Velqor5 Business Card - Health

Velqor5 maximizes value from the health data of its clients, including doctors, HMOs, and patients. I have attached the Velqor5 logo as an ai and eps file.
Target Market(s)
Health, HMO, Healthcare, Data, Big Data, Data Analytics
Industry/Entity Type
Business
Requirements
Must have
- At least one side should have some white on it so that we can write on it.

```html
<!DOCTYPE html>
<html lang="en">
<head>
<meta charset="utf-8">
<title>Velqor5 Business Card</title>
<link rel="stylesheet" href="https://fonts.googleapis.com/css2?family=Questrial&family=Open+Sans:wght@400;700&display=swap">
<style>
  :root {
    --bg: #e4e4e4;
    --card-black: #0d0e10;
    --card-black-soft: #1c1d20;
    --white: #ffffff;
    --blue: #1e8fe6;
    --blue-deep: #1673c9;
    --ink: #1f1f1f;
    --ink-soft: #444444;
  }
  * { box-sizing: border-box; margin: 0; padding: 0; }
  html, body {
    width: 1200px; height: 1200px; overflow: hidden;
    background: var(--bg);
  }
  .canvas {
    position: relative; width: 1200px; height: 1200px;
    display: flex; flex-direction: column; align-items: center; justify-content: center; gap: 70px;
  }
  .card {
    position: relative; width: 700px; height: 400px;
    border-radius: 26px; overflow: hidden;
    box-shadow: 0 10px 24px rgba(0,0,0,0.22);
  }
  .card--front {
    background:
      linear-gradient(100deg, transparent 28%, rgba(255,255,255,0.10) 38%, transparent 48%),
      linear-gradient(160deg, var(--card-black-soft), var(--card-black) 60%);
  }
  .brand {
    display: flex; align-items: center; gap: 26px;
    font-family: "Questrial", sans-serif; color: var(--white);
  }
  .brand__dot { background: var(--blue); border-radius: 50%; flex: none; }
  .card--front .brand {
    position: absolute; left: 200px; top: 150px;
  }
  .card--front .brand__dot { width: 92px; height: 92px; }
  .card--front .brand__name { font-size: 86px; line-height: 1; letter-spacing: 1px; }

  .card--back { background: var(--white); }
  .back__panel { position: absolute; inset: 0; width: 700px; height: 400px; }
  .card--back .brand {
    position: absolute; left: 125px; top: 200px;
    transform: translate(-50%, -50%) rotate(90deg);
    gap: 20px;
  }
  .card--back .brand__dot { width: 66px; height: 66px; }
  .card--back .brand__name { font-size: 64px; line-height: 1; }

  .details {
    position: absolute; left: 340px; top: 62px;
    font-family: "Open Sans", sans-serif; color: var(--ink);
  }
  .details__name { font-size: 30px; font-weight: 700; color: var(--blue); line-height: 1.1; }
  .details__title { font-size: 15px; color: var(--ink-soft); margin: 6px 0 0 22px; }
  .contacts { list-style: none; margin-top: 70px; margin-left: 22px; }
  .contacts li {
    display: flex; align-items: center; gap: 12px;
    font-size: 17px; line-height: 1.5;
  }
  .contacts svg { width: 16px; height: 16px; flex: none; fill: var(--blue); }
  .address { font-size: 17px; line-height: 1.4; margin: 8px 0 0 50px; }
</style>
</head>
<body>
<main class="canvas">
  <section class="card card--front" aria-label="Front of business card">
    <div class="brand">
      <span class="brand__dot"></span>
      <span class="brand__name">Velqor5</span>
    </div>
  </section>

  <section class="card card--back" aria-label="Back of business card">
    <svg class="back__panel" viewBox="0 0 700 400" aria-hidden="true">
      <defs>
        <linearGradient id="panelShade" x1="0" y1="0" x2="1" y2="1">
          <stop offset="0" stop-color="#1c1d20"/>
          <stop offset="0.6" stop-color="#0d0e10"/>
        </linearGradient>
      </defs>
      <path d="M0,0 H178 C210,120 305,210 310,400 H0 Z" fill="url(#panelShade)"/>
      <path d="M178,0 C210,120 305,210 310,400" fill="none" stroke="#1e8fe6" stroke-width="7"/>
    </svg>
    <div class="brand">
      <span class="brand__dot"></span>
      <span class="brand__name">Velqor5</span>
    </div>

    <div class="details">
      <p class="details__name">Your name</p>
      <p class="details__title">Your Title</p>
      <ul class="contacts">
        <li>
          <svg viewBox="0 0 16 16"><path d="M3 1h3l1.5 4-2 1.3a9 9 0 0 0 4.2 4.2L11 8.5l4 1.5v3a2 2 0 0 1-2 2A12 12 0 0 1 1 3a2 2 0 0 1 2-2z"/></svg>
          +00 111 222 3333
        </li>
        <li>
          <svg viewBox="0 0 16 16"><path d="M1 3h14v10H1z M2 4l6 5 6-5" fill="none" stroke="#1e8fe6" stroke-width="1.6"/></svg>
          yourname@yourwebsite.com
        </li>
        <li>
          <svg viewBox="0 0 16 16"><circle cx="8" cy="8" r="6.5" fill="none" stroke="#1e8fe6" stroke-width="1.4"/><path d="M1.5 8h13M8 1.5c-3 3.5-3 9.5 0 13M8 1.5c3 3.5 3 9.5 0 13" fill="none" stroke="#1e8fe6" stroke-width="1.2"/></svg>
          www.yourwebsite.com
        </li>
      </ul>
      <p class="address">Your Long Commercial or<br>business address in 2 line</p>
    </div>
  </section>
</main>
</body>
</html>
```